Business card for Harbor Crafters
Looking for creativity
Professional
Dominic Farrow
Owner Operator
47 S Pell Avenue
Middletown, DE 19842
@domfarrow
craftharborco@mailvane.com
www.craftharborco.com
Looking for a creative business card for my company. I have a logo and like the feel of it. The business card should have a contemporary feel and be interesting.
The name of the company and the website

```html
<!DOCTYPE html>
<html lang="en">
<head>
<meta charset="utf-8">
<title>Harbor Crafters Stationery</title>
<link href="https://fonts.googleapis.com/css2?family=Lato:wght@400;700&display=swap" rel="stylesheet">
<style>
  :root {
    --brand-blue: #2b4fa6;
    --brand-blue-light: #5b7fd0;
    --ink: #555c66;
    --rule: #8a8f96;
    --paper: #ffffff;
    --edge: #d9dce1;
    --backdrop: #ffffff;
  }
  * { box-sizing: border-box; margin: 0; padding: 0; }
  html, body { width: 1200px; height: 482px; overflow: hidden; background: var(--backdrop); }
  body { font-family: "Lato", sans-serif; color: var(--ink); position: relative; }

  .sheet, .envelope, .card {
    position: absolute; background: var(--paper); border: 1px solid var(--edge); overflow: hidden;
  }
  .brand-name {
    font-family: "Lato", sans-serif; font-weight: 700; color: var(--brand-blue);
    letter-spacing: 0.04em; line-height: 1;
  }
  .contact { font-size: 5px; line-height: 1.5; color: var(--ink); }
  .bottom-bands { position: absolute; left: 0; right: 0; }
  .bottom-bands .band-thin { height: 1px; background: var(--brand-blue-light); }
  .bottom-bands .band-thick { height: 3px; background: var(--brand-blue); margin-top: 2px; }

  /* fax cover sheet */
  .fax-sheet { left: 19px; top: 43px; width: 317px; height: 401px; }
  .fax-sheet .brand-name { position: absolute; left: 33px; top: 22px; font-size: 28px; }
  .fax-sheet .contact { position: absolute; left: 33px; top: 56px; }
  .fax-fields { position: absolute; left: 33px; top: 140px; width: 250px; display: grid; grid-template-columns: 1fr 1fr; row-gap: 12px; column-gap: 20px; }
  .fax-field { display: flex; align-items: flex-end; font-size: 6px; }
  .fax-field span { width: 24px; }
  .fax-field i { flex: 1; border-bottom: 1px solid var(--rule); height: 1px; }
  .fax-options { position: absolute; left: 33px; top: 230px; display: flex; gap: 9px; font-size: 5px; }
  .fax-options label { display: flex; align-items: center; gap: 2px; }
  .fax-options b { width: 5px; height: 5px; border: 1px solid var(--rule); display: inline-block; }
  .fax-sheet .bottom-bands { bottom: 14px; }

  /* envelopes */
  .envelope-front { left: 391px; top: 96px; width: 305px; height: 144px; }
  .envelope-front .brand-name { position: absolute; left: 20px; top: 14px; font-size: 22px; }
  .envelope-front .contact { position: absolute; left: 20px; top: 40px; }
  .envelope-front .bottom-bands { bottom: 10px; }
  .envelope-back { left: 391px; top: 283px; width: 305px; height: 144px; }
  .envelope-back svg.flap { position: absolute; left: 0; top: 0; }
  .envelope-back .brand-name { position: absolute; left: 0; right: 0; top: 22px; text-align: center; font-size: 20px; }
  .envelope-back .bottom-bands { bottom: 10px; }

  /* letterhead */
  .letterhead { left: 732px; top: 43px; width: 319px; height: 401px; }
  .letterhead .brand-name { position: absolute; left: 22px; top: 18px; font-size: 22px; }
  .letterhead .contact { position: absolute; left: 22px; top: 44px; }
  .letterhead .bottom-bands { bottom: 14px; }

  /* business cards */
  .card-front { left: 1070px; top: 108px; width: 106px; height: 65px; }
  .card-front .brand-name { position: absolute; left: 8px; top: 8px; font-size: 10px; }
  .card-front .person { position: absolute; left: 8px; top: 24px; font-size: 5px; line-height: 1.4; }
  .card-front .person strong { color: var(--brand-blue); font-size: 5.5px; }
  .card-front .bottom-bands { bottom: 5px; }
  .card-back { left: 1070px; top: 197px; width: 106px; height: 67px; background: var(--brand-blue); border-color: var(--brand-blue); }
  .card-back .brand-name { position: absolute; left: 0; right: 0; top: 24px; text-align: center; font-size: 13px; color: #fff; }
  .card-back .web { position: absolute; left: 0; right: 0; top: 40px; text-align: center; font-size: 4px; color: #dfe6f7; }
</style>
</head>
<body>

  <section class="sheet fax-sheet">
    <div class="brand-name">HARBOR</div>
    <div class="contact">47 S Pell Avenue, Middletown, DE 19842<br>craftharborco@mailvane.com<br>www.craftharborco.com</div>
    <div class="fax-fields">
      <div class="fax-field"><span>To:</span><i></i></div>
      <div class="fax-field"><span>From:</span><i></i></div>
      <div class="fax-field"><span>Fax:</span><i></i></div>
      <div class="fax-field"><span>Pages:</span><i></i></div>
      <div class="fax-field"><span>Phone:</span><i></i></div>
      <div class="fax-field"><span>Date:</span><i></i></div>
      <div class="fax-field"><span>Re:</span><i></i></div>
      <div class="fax-field"><span>CC:</span><i></i></div>
    </div>
    <div class="fax-options">
      <label><b></b>Urgent</label>
      <label><b></b>For Review</label>
      <label><b></b>Please Comment</label>
      <label><b></b>Please Reply</label>
      <label><b></b>Please Recycle</label>
    </div>
    <div class="bottom-bands"><div class="band-thin"></div><div class="band-thick"></div></div>
  </section>

  <section class="envelope envelope-front">
    <div class="brand-name">HARBOR</div>
    <div class="contact">47 S Pell Avenue, Middletown, DE 19842</div>
    <div class="bottom-bands"><div class="band-thin"></div><div class="band-thick"></div></div>
  </section>

  <section class="envelope envelope-back">
    <svg class="flap" width="305" height="144" viewBox="0 0 305 144" aria-hidden="true">
      <polyline points="0,0 152,70 305,0" fill="none" stroke="#c9ccd2" stroke-width="1"/>
    </svg>
    <div class="brand-name">HARBOR</div>
    <div class="bottom-bands"><div class="band-thin"></div><div class="band-thick"></div></div>
  </section>

  <section class="sheet letterhead">
    <div class="brand-name">HARBOR</div>
    <div class="contact">47 S Pell Avenue, Middletown, DE 19842<br>craftharborco@mailvane.com<br>www.craftharborco.com</div>
    <div class="bottom-bands"><div class="band-thin"></div><div class="band-thick"></div></div>
  </section>

  <section class="card card-front">
    <div class="brand-name">HARBOR</div>
    <div class="person"><strong>Dominic Farrow</strong><br>Owner Operator<br>craftharborco@mailvane.com<br>www.craftharborco.com</div>
    <div class="bottom-bands"><div class="band-thin"></div><div class="band-thick"></div></div>
  </section>

  <section class="card card-back">
    <div class="brand-name">HARBOR</div>
    <div class="web">www.craftharborco.com</div>
  </section>

</body>
</html>
```